We need a range of stationery items designed for our active, community-orientated, out-going, all-age, family-friendly church in central Auckland, New Zealand.
We want to refresh and modernize the branding/images for Kereru Gospel Chapel itself so this image reflects who we are and our values.
Our church is located on a very busy intersection in the heart of a multi-ethnic local community. A number of churches and other groups use our site so we have branded our site as "The Meeting Pole". We have an existing logo for "The Meeting Pole" (see attached).
We would like you to design 4 items: a Letterhead, a With Compliments slip, a Business Card, and the Front Cover of our church newsletter, but we've included a request for an Email signature as an optional extra for this brief.
Organisation Details:
Name: Kereru Gospel Chapel
Postal Address: PO Box 38514, Wharenui, Auckland 1893
Email: office@kererugospel.org.nz
Phone: 09 473 5619
Web: www.kererugospel.org.nz (current website will be changed)
Position Statement: "a place of hope, belonging and worship"
Fonts:
The fonts for the "The Meeting Pole" logo are Futura Medium BT and Futura Lt BT. We would like the Futura font family used in the designs but feel free to add other fonts as appropriate (preferably True Type open source ones).
Colours:
Our current external signage colours are Dark Grey (Tolvar Coatings 'Slatewick' - RGB 57-55-53 ) and orange ( Tolvar 'Sunflare' - RGB 255-82-0 ). These are the colours for 'The Meeting Pole' which is our site. As we have other churches using our premises also we are looking to create a separate but complimentary identity for Kereru Gospel Chapel with a different colour set. We would ideally like a primary colour, a complimentary colour and an offset colour.
Design:
For the Kereru Gospel Chapel stationary we want the design to incorporate some of the elements of the 'Meeting Pole' particularly the extended 'T' device, so that we develop a separate identity but in the same family. We would like something that will look good for a number of years, rather than something that will date quickly in a year or two as fashions change.
PROJECTS
1. Letterhead
Finished size A4 (210 mm wide x 297mm tall)
This will become a template in MSWord. It will be printed in colour on our office photocopier so it must have a 5mm white border around the entire outside edge of the A4 page. "The Meeting Pole" logo needs to be incorporated in some form on the page.
2. With Compliments slip
Finished size 210 mm wide x 99 mm tall
This will be printed in colour on our office photocopier so it must have a 5mm white border around the entire outside edge of the slip. We will print these slips 3-up on an A4 page. The actual design space will be 200mm x 89mm. It is envisaged that this slip will use the same elements as the letterhead design. Please supply two versions, with and without the words "With Compliments".
3. Business Card
Finished size 90 mm wide by 55 mm tall.
This will be printed by commercial printers so colours can run to the edge of the card. Your Kereru Gospel Logo with the extended 'T' devise will need to feature on this.
4. Front Cover of Church Newsletter
Finished size 100 mm wide x 210 mm tall.
Our newsletter is printed in landscape on A4 paper and is folded twice.
It will be printed in colour on our office photocopier so it will need to have a minimum 5mm white border on all 4 sides. Attractive inviting colours preferred.
Needs to have:
- a place for the words Sunday and a date (which will change each Sunday)
- your Kereru Gospel Logo with the extended 'T' devise
- the words Sundays @ 10am
- the words ""a place of hope, belonging and worship"
- optional - "The Meeting Pole" logo (background does not need to be black)
5. Email Signature - optional extra
Not too large but something that will enable those receiving emails to instantly recognize who the email is from. Needs to include your Kereru Gospel logo, the name of the person, their position and our contact details.
Reason: We are extending the deadline on this project in order to encourage a broader range of designs, both from those who have already submitted designs and from those who are considering entering our competition. We'd love to see what you have to offer so please do submit your designs.
Re: Stationery for Kereru Gospel Chapel
Thanks to all the designers who have submitted designs for our competition so far. We have refrained from requesting a whole lot of tweaks to individual designs out of respect for your time as we understand that you are all busy professionals and that design competitions like this are just one way that you pitch for new business.
We would though like to offer some general comments on the submissions that we have seen so far. One thing that we would definitely like to arrive at via this process is to decide on a colour scheme. For this, as per the brief notes ( but possibly obscured by some of the other detail ) we want to have a primary colour and an offset colour and also an accent colour in the pallet.
Another thing that we maybe didn't make clear enough is that the colours for the identity of the site, known as The Meeting Pole, uses dark grey and orange but that we wanted to develop a separate but related identity for Kereru Gospel Chapel that meets there as we also now have other congregations that use our buildings.
One of the keys for the new identity will be the new colour pallet which we wanted to steer away from the darker tones that we used for the site branding. Therefore we would very much like to see your suggestions one or two secondary colours along with the primary brand colour if possible please.
Thank you all once again.
Kind regards

```html
<!DOCTYPE html>
<html lang="en">
<head>
<meta charset="utf-8">
<title>Kereru Gospel Chapel – Newsletter Cover</title>
<link rel="stylesheet" href="https://fonts.googleapis.com/css2?family=Jost:wght@300;400;500&display=swap">
<style>
  :root {
    --crimson: #7a1519;
    --crimson-dark: #4f0c0f;
    --rose: #d4968e;
    --blush: #ddb6b0;
    --blush-light: #e6c6c1;
    --blush-deep: #d3a7a1;
    --paper: #ffffff;
  }
  * { margin: 0; padding: 0; box-sizing: border-box; }
  html, body {
    width: 1200px;
    height: 2396px;
    overflow: hidden;
    background: var(--paper);
  }
  body { font-family: "Jost", "Futura", sans-serif; position: relative; }

  .cover-frame {
    position: absolute;
    left: 20px; top: 108px;
    width: 1068px; height: 2180px;
    border: 3px solid var(--crimson);
  }

  .issue-band {
    position: absolute;
    left: 20px; top: 108px;
    width: 1068px; height: 60px;
    background: var(--crimson);
    color: var(--paper);
    font-weight: 300;
    font-size: 38px;
    line-height: 60px;
    padding-left: 20px;
  }

  .church-name {
    position: absolute;
    left: 0; top: 254px;
    width: 1200px;
    text-align: center;
    color: var(--crimson);
    font-weight: 400;
    font-size: 58px;
    letter-spacing: 0.75em;
    padding-left: 0.75em;
    line-height: 1;
  }

  .service-ribbon {
    position: absolute;
    left: 328px; top: 456px;
    width: 544px; height: 140px;
  }
  .service-ribbon span {
    position: absolute;
    left: 72px; top: 8px;
    width: 400px; height: 104px;
    line-height: 104px;
    text-align: center;
    color: var(--paper);
    font-weight: 300;
    font-size: 38px;
    letter-spacing: 0.03em;
  }

  .feature-art {
    position: absolute;
    left: 180px; top: 780px;
    width: 848px; height: 840px;
    background: radial-gradient(ellipse at 50% 50%, var(--blush-light) 0%, var(--blush) 55%, var(--blush-deep) 100%);
  }

  .tagline-band {
    position: absolute;
    left: 20px; top: 1792px;
    width: 1068px; height: 56px;
    background: var(--crimson);
    color: var(--paper);
    text-align: center;
    font-weight: 300;
    font-size: 36px;
    line-height: 56px;
    letter-spacing: 0.02em;
    padding-left: 44px;
  }

  .chapel-mark {
    position: absolute;
    left: 0; top: 1930px;
    width: 1200px;
    height: 260px;
    display: flex;
    align-items: center;
    justify-content: center;
    gap: 30px;
  }
  .chapel-mark .dot {
    width: 120px; height: 120px;
    border-radius: 50%;
    background: var(--crimson);
  }
  .chapel-mark .name {
    color: var(--crimson);
    font-weight: 400;
    font-size: 60px;
    letter-spacing: 0.04em;
  }
</style>
</head>
<body>
  <div class="cover-frame"></div>

  <div class="issue-band">Sunday date -- Volume X</div>

  <h1 class="church-name">KERERU</h1>

  <div class="service-ribbon">
    <svg width="544" height="140" viewBox="0 0 544 140" aria-hidden="true">
      <polygon points="0,32 100,32 100,136 0,136 36,84" fill="var(--rose)"/>
      <polygon points="544,32 444,32 444,136 544,136 508,84" fill="var(--rose)"/>
      <polygon points="72,112 100,112 100,136" fill="var(--crimson-dark)"/>
      <polygon points="472,112 444,112 444,136" fill="var(--crimson-dark)"/>
      <rect x="72" y="8" width="400" height="104" fill="var(--crimson)"/>
    </svg>
    <span>Sundays @ 10 AM</span>
  </div>

  <div class="feature-art" role="img" aria-label="Feature artwork: hand-lettered word in soft grey script on a blush pink square"></div>

  <div class="tagline-band">A place of hope, belonging and worship</div>

  <div class="chapel-mark">
    <div class="dot"></div>
    <div class="name">Kereru Gospel</div>
  </div>
</body>
</html>
```